Korvel CD Cover Design Project

I need a CD front cover(front inlay) , CD top artwork, CD back cover (back inlay)
i have provided a picture and other
Artiste Name: Korvel
Song Title: Olufunke (carry me Away)
Producer: trokay
Track-list
1. Olufunke (carry me Away)
2. Olufunke (carry me Away) acapella
3. Olufunke (carry me Away) (Instrumental)
stay connected:
chirpline.com/miloskorvel
friendwall.com/miloskorvel
www.korvel-music.com
Management contact:
USA : Marla @ +15550148832 / marla@brightwavepr.com
UK: Tamsin @ +447700900417/ +447700900283 / tamsinbookings@mailhaven.co.uk
Nigeria: Funmi @ +2348000314729 / funmi@korvel-music.com
Target Market(s)
african Music consumers globally
Industry/Entity Type
Management
Look and feel
Each slider illustrates characteristics of the customer's brand and the style your logo design should communicate.

```html
<!DOCTYPE html>
<html lang="en">
<head>
<meta charset="utf-8">
<title>Korvel – Olufunke (carry me Away) CD Inlay</title>
<link href="https://fonts.googleapis.com/css2?family=Berkshire+Swash&family=Playball&family=Courgette&display=swap" rel="stylesheet">
<style>
  :root {
    --paper: #ffffff;
    --ink: #111111;
    --sky-top: #6f9fb8;
    --sky-mid: #c9d8da;
    --sea: #2f8f98;
    --surf: #bcd6cf;
    --sand: #b59a6a;
    --sand-dark: #8c7449;
    --panel: rgba(255, 255, 255, 0.78);
    --portrait: #2b2b2b;
    --link-mark: #3b79b5;
  }
  html, body {
    margin: 0;
    padding: 0;
    width: 1200px;
    height: 582px;
    overflow: hidden;
    background: var(--paper);
  }
  .inlay {
    position: relative;
    width: 1200px;
    height: 582px;
    background: var(--paper);
  }
  .beach-artwork {
    position: absolute;
    left: 52px;
    top: 37px;
    width: 1098px;
    height: 500px;
    background: linear-gradient(180deg,
      var(--sky-top) 0%,
      var(--sky-mid) 28%,
      var(--sea) 40%,
      var(--surf) 56%,
      var(--sand) 74%,
      var(--sand-dark) 100%);
    overflow: hidden;
  }
  .portrait-artwork {
    position: absolute;
    left: 700px;
    top: 135px;
    width: 350px;
    height: 330px;
    border-radius: 46% 46% 50% 50%;
    background: radial-gradient(ellipse at 50% 55%, rgba(43,43,43,0.75) 0%, rgba(43,43,43,0.35) 55%, rgba(43,43,43,0) 75%);
  }
  .artist-name {
    position: absolute;
    left: 752px;
    top: 66px;
    width: 310px;
    text-align: center;
    margin: 0;
    font-family: "Berkshire Swash", cursive;
    font-weight: 400;
    font-size: 50px;
    line-height: 60px;
    letter-spacing: 3px;
    color: var(--ink);
  }
  .song-title {
    position: absolute;
    left: 740px;
    top: 382px;
    width: 360px;
    text-align: center;
    margin: 0;
    font-family: "Playball", cursive;
    font-weight: 400;
    color: var(--ink);
    line-height: 1;
  }
  .song-title .name { display: block; font-size: 58px; }
  .song-title .subtitle { display: block; font-size: 30px; margin-top: 14px; }
  .tracklist {
    position: absolute;
    left: 120px;
    top: 64px;
    margin: 0;
    padding: 0;
    list-style: none;
    font-family: "Berkshire Swash", cursive;
    font-size: 21px;
    color: var(--ink);
  }
  .track {
    position: relative;
    width: 270px;
    text-align: center;
    line-height: 29px;
    margin-bottom: 18px;
  }
  .track.second { left: 14px; }
  .track .length {
    position: absolute;
    left: 255px;
    top: 0;
    font-size: 20px;
  }
  .info-panel {
    position: absolute;
    left: 62px;
    top: 346px;
    width: 490px;
    height: 186px;
    background: var(--panel);
  }
  .producer {
    position: absolute;
    left: 250px;
    top: 6px;
    margin: 0;
    font-family: "Playball", cursive;
    font-size: 22px;
    color: var(--ink);
  }
  .connect {
    position: absolute;
    left: 188px;
    top: 42px;
    margin: 0;
    font-family: "Courgette", cursive;
    font-size: 14px;
    line-height: 18px;
    color: var(--ink);
  }
  .connect .label { display: block; }
  .connect .link { display: block; padding-left: 12px; }
  .connect .link.channel { padding-left: 0; }
  .link-mark {
    display: inline-block;
    width: 11px;
    height: 11px;
    margin-right: 6px;
    vertical-align: -1px;
    background: var(--link-mark);
  }
  .management {
    position: absolute;
    left: 24px;
    top: 104px;
    margin: 0;
    font-family: "Courgette", cursive;
    font-size: 10.5px;
    line-height: 20px;
    color: var(--ink);
  }
  .management .label { display: block; font-size: 11px; line-height: 16px; margin-bottom: 2px; }
</style>
</head>
<body>
<main class="inlay">
  <div class="beach-artwork" role="img" aria-label="Weathered photograph of a tropical beach with sky, turquoise sea and sand">
    <div class="portrait-artwork" role="img" aria-label="Stencil-style portrait illustration of the artist"></div>
  </div>

  <ol class="tracklist">
    <li class="track">1. Olufunke<span class="length">3.45</span><br>(carry me Away)</li>
    <li class="track second">2. Olufunke<span class="length">4.02</span><br>(carry me Away)<br>acapella</li>
    <li class="track">3. Olufunke<span class="length">5.11</span><br>(carry me Away)<br>(Instrumental)</li>
  </ol>

  <h1 class="artist-name">KORVEL</h1>

  <h2 class="song-title">
    <span class="name">Olufunke</span>
    <span class="subtitle">( carry me Away )</span>
  </h2>

  <section class="info-panel">
    <p class="producer">Produced by trokay</p>
    <p class="connect">
      <span class="label">stay connected:</span>
      <span class="link">www.korvel-music.com</span>
      <span class="link channel"><span class="link-mark"></span>chirpline.com/miloskorvel</span>
      <span class="link channel"><span class="link-mark"></span>friendwall.com/miloskorvel</span>
    </p>
    <p class="management">
      <span class="label">Management contact:</span>
      USA : Marla @ +15550148832 / marla@brightwavepr.com<br>
      UK : Tamsin @ +447700900417/ +447700900283 / tamsinbookings@mailhaven.co.uk<br>
      Nigeria : Funmi @ +2348000314729 / funmi@korvel-music.com
    </p>
  </section>
</main>
</body>
</html>
```